Banner Ad Design Project

hi i need several banner for a casino website
for examples you can visit some of the online casinos on the net.

the banners i need:

1. sportsbook
2. live casino
3. blackjack
4. slot games
5. bonus (e.g. Christmass bonus "double your deposit!" or "free spins"
6. "Do you want to win a trip to Las Vegas? Join now!"

if possible with some movement (flash/html5)
Updates

i have updated the prices!

payment committed! 

Project Deadline Extended
Reason: Error by makerhive End day was similar on start day

Industry/Entity Type

Casino

```html
<!DOCTYPE html>
<html lang="en">
<head>
<meta charset="utf-8">
<title>Casino Banner Set</title>
<link rel="stylesheet" href="https://fonts.googleapis.com/css2?family=Source+Sans+3:wght@700&family=PT+Sans+Narrow:wght@700&display=swap">
<style>
  :root {
    --page-bg: #ffffff;
    --gold-light: #f6e7b0;
    --gold: #d6a52a;
    --gold-deep: #b8861b;
    --panel-dark: #2e2f2f;
    --panel-mid: #4b4c4c;
    --text-white: #ffffff;
    --text-gold: #e0c18c;
    --text-gold-deep: #b58a4e;
  }
  * { box-sizing: border-box; margin: 0; padding: 0; }
  html, body {
    width: 1200px;
    height: 1073px;
    overflow: hidden;
    background: var(--page-bg);
  }
  .canvas { position: relative; width: 1200px; height: 1073px; }

  .banner {
    position: absolute;
    width: 903px;
    height: 122px;
    padding: 5px;
    background: linear-gradient(90deg, var(--gold-deep) 0%, var(--gold) 30%, var(--gold-light) 55%, var(--gold) 75%, var(--gold-deep) 100%);
    display: flex;
  }
  .banner-photo { width: 544px; height: 100%; flex: none; }
  .banner-panel {
    flex: 1;
    height: 100%;
    background: linear-gradient(90deg, var(--panel-dark) 0%, var(--panel-mid) 45%, var(--panel-dark) 100%);
    display: flex;
    flex-direction: column;
    align-items: center;
    justify-content: center;
    font-family: "Source Sans 3", sans-serif;
    font-weight: 700;
    line-height: 0.88;
    text-align: center;
    white-space: nowrap;
  }
  .title-white { color: var(--text-white); font-size: 46px; }
  .title-white-small { color: var(--text-white); font-size: 38px; }
  .title-gold {
    font-size: 44px;
    background: linear-gradient(180deg, var(--text-gold) 0%, var(--text-gold-deep) 100%);
    -webkit-background-clip: text;
    background-clip: text;
    color: transparent;
  }

  .banner--live-casino { left: 174px; top: 17px; }
  .banner--blackjack   { left: 175px; top: 167px; }
  .banner--slots       { left: 175px; top: 319px; }
  .banner--sportsbook  { left: 174px; top: 472px; }
  .banner--bonus       { left: 175px; top: 613px; }
  .banner--vegas       { left: 179px; top: 763px; }

  .photo--roulette {
    background:
      radial-gradient(ellipse 22% 70% at 17% 35%, rgba(240,190,70,0.95), rgba(240,190,70,0) 70%),
      radial-gradient(ellipse 60% 40% at 65% 55%, rgba(225,40,30,0.9), rgba(225,40,30,0) 75%),
      radial-gradient(ellipse 40% 30% at 50% 95%, rgba(230,170,60,0.7), rgba(230,170,60,0) 80%),
      linear-gradient(160deg, #3a0a06 0%, #8e1c12 45%, #c8301c 70%, #6a140c 100%);
  }
  .photo--cards {
    background:
      radial-gradient(ellipse 20% 80% at 27% 70%, rgba(238,236,228,1), rgba(238,236,228,0) 75%),
      radial-gradient(ellipse 15% 60% at 52% 100%, rgba(220,218,210,0.8), rgba(220,218,210,0) 75%),
      radial-gradient(ellipse 18% 45% at 68% 90%, rgba(190,60,55,0.85), rgba(190,60,55,0) 75%),
      linear-gradient(180deg, #1e9a58 0%, #168a4c 100%);
  }
  .photo--slots {
    background:
      radial-gradient(ellipse 16% 45% at 20% 30%, rgba(90,170,110,0.6), rgba(90,170,110,0) 75%),
      radial-gradient(ellipse 12% 40% at 42% 45%, rgba(120,160,130,0.5), rgba(120,160,130,0) 75%),
      radial-gradient(ellipse 35% 80% at 78% 50%, rgba(232,180,130,0.9), rgba(232,180,130,0) 75%),
      linear-gradient(90deg, #5a2c16 0%, #3a2620 35%, #6a3a22 60%, #9a5a30 100%);
  }
  .photo--football {
    background:
      radial-gradient(ellipse 10% 30% at 27% 30%, rgba(150,70,40,0.9), rgba(150,70,40,0) 80%),
      radial-gradient(ellipse 22% 60% at 58% 70%, rgba(220,110,40,0.9), rgba(220,110,40,0) 75%),
      radial-gradient(ellipse 30% 60% at 85% 40%, rgba(200,195,190,0.5), rgba(200,195,190,0) 75%),
      linear-gradient(90deg, #6e6878 0%, #8a7e80 40%, #7a7482 70%, #5e5a6a 100%);
  }
  .photo--snow-game {
    background:
      radial-gradient(ellipse 22% 70% at 40% 60%, rgba(40,55,55,0.85), rgba(40,55,55,0) 75%),
      radial-gradient(ellipse 25% 70% at 72% 65%, rgba(235,238,242,0.95), rgba(235,238,242,0) 75%),
      radial-gradient(ellipse 12% 30% at 55% 25%, rgba(90,140,200,0.5), rgba(90,140,200,0) 80%),
      linear-gradient(90deg, #7a7a72 0%, #8c8e86 40%, #a6a8a4 100%);
  }
  .photo--vegas {
    background:
      radial-gradient(ellipse 18% 70% at 62% 55%, rgba(240,170,70,0.95), rgba(240,170,70,0) 75%),
      radial-gradient(ellipse 10% 50% at 40% 70%, rgba(60,90,220,0.7), rgba(60,90,220,0) 80%),
      radial-gradient(ellipse 40% 40% at 30% 90%, rgba(220,140,60,0.6), rgba(220,140,60,0) 80%),
      radial-gradient(ellipse 10% 60% at 95% 55%, rgba(230,170,90,0.8), rgba(230,170,90,0) 80%),
      linear-gradient(180deg, #1a1a28 0%, #2a2230 45%, #4a3020 100%);
  }

  .banner--live-casino .live-word { font-size: 38px; }

  .banner--bonus .banner-panel { line-height: 1.0; }
  .banner--bonus .title-white-small { font-size: 37px; }
  .banner--bonus .title-gold { font-size: 36px; letter-spacing: -0.6px; }

  .banner--vegas .banner-photo { width: 505px; }
  .banner--vegas .banner-panel {
    font-family: "PT Sans Narrow", sans-serif;
    align-items: stretch;
    padding: 4px 4px 0 4px;
    line-height: 0.86;
  }
  .vegas-line-1 { color: var(--text-white); font-size: 40px; text-align: left; }
  .vegas-line-2 { color: var(--text-white); font-size: 40px; text-align: right; }
  .vegas-cta { font-size: 54px; text-align: center; line-height: 0.82; }
</style>
</head>
<body>
<main class="canvas">
  <section class="banner banner--live-casino">
    <div class="banner-photo photo--roulette" role="img" aria-label="Close-up of a spinning roulette wheel with numbered pockets"></div>
    <div class="banner-panel">
      <span class="title-white">online</span>
      <span><span class="title-white live-word">live </span><span class="title-gold">casino</span></span>
    </div>
  </section>

  <section class="banner banner--blackjack">
    <div class="banner-photo photo--cards" role="img" aria-label="Ace and jack playing cards on a green felt table with a casino chip"></div>
    <div class="banner-panel">
      <span class="title-white">online</span>
      <span class="title-gold">blackjack</span>
    </div>
  </section>

  <section class="banner banner--slots">
    <div class="banner-photo photo--slots" role="img" aria-label="Excited players celebrating beside a row of slot machines"></div>
    <div class="banner-panel">
      <span class="title-white">online</span>
      <span class="title-gold">slots</span>
    </div>
  </section>

  <section class="banner banner--sportsbook">
    <div class="banner-photo photo--football" role="img" aria-label="Quarterback throwing a football in front of a stadium crowd"></div>
    <div class="banner-panel">
      <span class="title-white">online</span>
      <span class="title-gold">sportsbook</span>
    </div>
  </section>

  <section class="banner banner--bonus">
    <div class="banner-photo photo--snow-game" role="img" aria-label="Football players tackling during a snowy winter game"></div>
    <div class="banner-panel">
      <span class="title-white-small">Christmass Bonus</span>
      <span class="title-gold">Double Your Deposit!</span>
    </div>
  </section>

  <section class="banner banner--vegas">
    <div class="banner-photo photo--vegas" role="img" aria-label="Aerial night view of the illuminated Las Vegas strip"></div>
    <div class="banner-panel">
      <span class="vegas-line-1">Do you want to win</span>
      <span class="vegas-line-2">a trip to Las Vegas?</span>
      <span class="title-gold vegas-cta">Join now!</span>
    </div>
  </section>
</main>
</body>
</html>
```